New Lead input page design

Attached is our concept of a new lead input screen for the back-end of our website which is a tool for a loan agent (2 page PDF attached)

1. This is the first of many other data input screen projects for our website, so the designer that ends up with us will have quite a bit of add on new projects.

2. HERE IS THE LINK WITH THE SAMPLE OF ALL THE CURRENT CONTROLS:
http://apps.brimtally88.net/controlWidgets.html

3. The colors and hues of: either GREEN & GREYS or BLUE & GREYS.

4. I think some gradients and shadows adds depth and sophistication. Basically trying to get away from old school flat, one dimensional data screen inputs and add some design flare to it.

5. Upon completion we will need the HTML of the design etc and we will code the input fields directly.

6. See attached files for the entire input screen. Please also add the data input space (see sample) to your design.

Thank you

Reason: We are extending the deadline to give us time to ask current designs to complete slight revisions

Reason: Finalizing the selection for one last variation detailed to current designers

```html
<!DOCTYPE html>
<html lang="en">
<head>
<meta charset="utf-8">
<title>New Lead Input</title>
<link href="https://fonts.googleapis.com/css2?family=Source+Sans+3:wght@400;600;700&display=swap" rel="stylesheet">
<style>
  :root {
    --brand: #4d87dc;
    --brand-dark: #3a6fc0;
    --badge: #4a80d8;
    --page: #ededed;
    --card: #ffffff;
    --label: #141414;
    --value: #3a3a3a;
    --white: #ffffff;
  }
  * { box-sizing: border-box; margin: 0; padding: 0; }
  html, body {
    width: 1200px; height: 800px; overflow: hidden;
    background: var(--page);
    font-family: "Source Sans 3", "Source Sans Pro", sans-serif;
  }
  .screen {
    position: relative; width: 1200px; height: 800px; overflow: hidden;
    background: var(--page);
  }
  .top-bar {
    position: absolute; left: 0; top: 0; width: 1200px; height: 121px;
    background: var(--brand);
    border-bottom: 1px solid var(--brand-dark);
  }
  .nav-item {
    position: absolute; top: 47px; height: 26px;
    display: flex; align-items: center; gap: 7px;
    color: var(--white); font-size: 17px; font-weight: 600;
    letter-spacing: -0.3px; white-space: nowrap;
    text-shadow: 0 1px 1px rgba(0,0,0,0.25);
  }
  .nav-item svg { width: 22px; height: 22px; fill: var(--white); flex: none; }
  .lead-card {
    position: absolute; left: 120px; width: 960px; height: 150px;
    background: var(--card); border-radius: 4px;
    box-shadow: 0 1px 4px rgba(0,0,0,0.12);
  }
  .badge {
    position: absolute; left: 29px; top: 35px; width: 80px; height: 80px;
    border-radius: 50%; background: var(--badge);
    box-shadow: 0 2px 3px rgba(0,0,0,0.18);
    display: flex; align-items: center; justify-content: center; text-align: center;
    color: var(--white); font-size: 15px; line-height: 19px; letter-spacing: -0.3px;
  }
  .field-grid {
    position: absolute; left: 148px; top: 29px;
    display: grid; grid-template-columns: 185px 217px 187px auto;
    grid-auto-rows: 22px; font-size: 17px; line-height: 22px; white-space: nowrap;
  }
  .field-label { color: var(--label); font-weight: 700; }
  .field-value { color: var(--value); }
  .inline-pair { display: flex; gap: 21px; }
  .add-borrower {
    position: absolute; left: 551px; top: 90px; width: 120px; height: 33px;
    background: var(--brand); border: 1px solid var(--brand-dark); border-radius: 2px;
    color: var(--white); font-family: inherit; font-size: 13px; font-weight: 600;
  }
</style>
</head>
<body>
<div class="screen">
<header class="top-bar">
  <div class="nav-item" style="left:144px">
    <svg viewBox="0 0 22 22"><path d="M10.3 1h1.4v17l3-3 1 1-4.7 4.7L6.3 16l1-1 3 3z"/></svg>Lead Category</div>
  <div class="nav-item" style="left:308px">
    <svg viewBox="0 0 22 22"><path d="M4 3h4V1.5h6V3h4v18H4zm2 2v14h10V5h-2v1.5H8V5zm2 3h6v1.5H8zm0 3h6v1.5H8zm0 3h6v1.5H8z"/></svg>Sticky Note</div>
  <div class="nav-item" style="left:458px">
    <svg viewBox="0 0 22 22"><path d="M2 3h18v12H8l-4 4v-4H2zm3 3v1.5h12V6zm0 3v1.5h12V9z"/></svg>Snapshot</div>
  <div class="nav-item" style="left:584px">
    <svg viewBox="0 0 22 22"><path d="M2 8h4l10-5v16L6 14H5l1.5 5h-3L2 14zm16 1h3v4h-3z"/></svg>Alerts</div>
  <div class="nav-item" style="left:683px">
    <svg viewBox="0 0 22 22"><path d="M5 4h12l4 9v6H1v-6zm1.3 2L3.6 12H8l1 2h4l1-2h4.4l-2.7-6z"/></svg>Lead Notes</div>
  <div class="nav-item" style="left:822px">
    <svg viewBox="0 0 22 22"><path d="M2 3h3V1h2v2h8V1h2v2h3v18H2zm2 5v11h14V8zm2 2h2v2H6zm4 0h2v2h-2zm4 0h2v2h-2zm-8 4h2v2H6zm4 0h2v2h-2zm4 0h2v2h-2z"/></svg>Calendar</div>
</header>

<main>
  <section class="lead-card" style="top:178px">
    <div class="badge">Clients</div>
    <div class="field-grid">
      <span class="field-label">Borrower:</span><span class="field-value">Daniel Marsh</span>
      <span class="field-label">Co-Borrower:</span><span class="field-value">Daniel Marsh</span>
      <span class="field-label">Application:</span><span class="field-value">Joint</span>
      <span class="field-label">Relationship:</span><span class="field-value">Joint</span>
      <span class="field-label">Lead Stat:</span><span class="field-value">3</span><span></span><span></span>
      <span class="field-label">Demo Stat:</span><span class="field-value">4</span><span></span><span></span>
    </div>
    <button class="add-borrower">Add Borrower</button>
  </section>

  <section class="lead-card" style="top:358px">
    <div class="badge">Existing<br>Loan</div>
    <div class="field-grid">
      <span class="field-label">Current Amount:</span><span class="field-value">$335,758</span>
      <span class="field-label">How many loans:</span>
      <span class="inline-pair"><span class="field-value">2</span><span><span class="field-label">Pay off Both?</span>&nbsp;&nbsp; <span class="field-value">Yes</span></span></span>
      <span class="field-label">Current Loan:</span><span class="field-value">&nbsp;30 year fix – 5.5%</span>
      <span class="field-label">Current P &amp; I:</span><span class="field-value">$2,200</span>
      <span class="field-label">Apprx. Last Refi:</span><span class="field-value">&nbsp;4 years ago</span>
      <span class="field-label">Tax &amp; Insurance:</span><span class="field-value">$450</span>
      <span class="field-label">Add more Loans:</span><span class="field-value">$59,000 - Heloc</span>
      <span class="field-label">Total Payment:</span><span class="field-value">$2,650</span>
    </div>
  </section>

  <section class="lead-card" style="top:543px">
    <div class="badge">Clients</div>
    <div class="field-grid">
      <span class="field-label">Borrower:</span><span class="field-value">Daniel Marsh</span>
      <span class="field-label">Co-Borrower:</span><span class="field-value">Daniel Marsh</span>
      <span class="field-label">Application:</span><span class="field-value">Joint</span>
      <span class="field-label">Relationship:</span><span class="field-value">Joint</span>
      <span class="field-label">Lead Stat:</span><span class="field-value">3</span><span></span><span></span>
      <span class="field-label">Demo Stat:</span><span class="field-value">4</span><span></span><span></span>
    </div>
    <button class="add-borrower">Add Borrower</button>
  </section>

  <section class="lead-card" style="top:734px">
    <div class="badge">Existing<br>Loan</div>
    <div class="field-grid" style="top:26px">
      <span class="field-label">Current Amount:</span><span class="field-value">$335,758</span>
      <span class="field-label">How many loans:</span>
      <span class="inline-pair"><span class="field-value">2</span><span><span class="field-label">Pay off Both?</span>&nbsp;&nbsp; <span class="field-value">Yes</span></span></span>
      <span class="field-label">Current Loan:</span><span class="field-value">&nbsp;30 year fix – 5.5%</span>
      <span class="field-label">Current P &amp; I:</span><span class="field-value">$2,200</span>
    </div>
  </section>
</main>
</div>
</body>
</html>
```